HIgh-end jewelry designer needs a business card design

I need a business card design for the ecclectic & rather expensive jewelry designs. My approach to my work is to combine very old jewelry offset with contemporary items. I enjoy the idea of legacy as well as repurposing finely crafted items that are not possible to create any longer. My desire is to celebrate the past in a contemporary & funky way. The name of my business is VELLORINE. I see my business card design as simple & yet enigmatic as possible. In the end... clean, simple & understated is the look I am after. Thank you for your consideration...

Target Market(s)

I will use this business card for the trade as well as customers

Industry/Entity Type

Business

Contact Information for Business Card

Marta Quorrin Owner/Designer 555-203-7718

Requirements
Must have
• Clean & simple sophisticated design using the word "Vellorinne" as the logo. I like the idea of a play on the word itself, perhaps even using different fonts (i.e.: a bold helvetica combined with a lovely script). I'm afraid to say more because I don't want to limit creative input. Gosh, sometimes it's ok to break the rules!
Nice to have
• In my mind, I have imagined this business card to be simple, using my company name "Vellorine" in a playful yet sophisticated manner. I believe that doing something beautifully simple can be a true challenge. I have imagined something with just black & white, however I am open to ideas... after all that's why I'm here!
Should not have
• As Mozart once said... "It has too many notes!" I know I'm being silly, but I don't want it to be complicated or overly ornate.

```html
<!DOCTYPE html>
<html lang="en">
<head>
<meta charset="utf-8">
<title>Vellorine — Business Card</title>
<link rel="stylesheet" href="https://fonts.googleapis.com/css2?family=Dancing+Script:wght@500&family=Josefin+Sans:wght@300;400&display=swap">
<style>
  :root {
    --backdrop: #e4e2df;
    --card: #0b0b0b;
    --ink: #f2f2f2;
    --muted: #8c8c8c;
    --rule: #d9d9d9;
  }
  * { margin: 0; padding: 0; box-sizing: border-box; }
  html, body {
    width: 1200px;
    height: 902px;
    overflow: hidden;
    background: var(--backdrop);
  }
  .stage {
    width: 1200px;
    height: 902px;
    display: flex;
    align-items: center;
    justify-content: center;
  }
  .card {
    position: relative;
    width: 840px;
    height: 480px;
    background: var(--card);
    box-shadow: 0 18px 40px rgba(0,0,0,0.25);
    color: var(--ink);
    font-family: "Josefin Sans", sans-serif;
  }
  .holder-name {
    position: absolute;
    left: 112px;
    top: 78px;
    font-family: "Dancing Script", cursive;
    font-weight: 500;
    font-size: 38px;
    color: var(--ink);
  }
  .holder-role {
    position: absolute;
    left: 150px;
    top: 132px;
    font-size: 17px;
    font-weight: 300;
    letter-spacing: 0.5px;
    color: var(--muted);
  }
  .wordmark {
    position: absolute;
    left: 92px;
    top: 168px;
    font-size: 128px;
    font-weight: 300;
    line-height: 1;
    letter-spacing: 2px;
    color: var(--ink);
  }
  .bracket {
    position: absolute;
    left: 150px;
    top: 312px;
  }
  .contact {
    position: absolute;
    top: 346px;
    display: flex;
    align-items: center;
    gap: 10px;
    font-size: 19px;
    font-weight: 400;
    letter-spacing: 0.5px;
    color: var(--ink);
  }
  .contact-phone { left: 150px; }
  .contact-email { left: 470px; }
  .contact-divider {
    position: absolute;
    left: 430px;
    top: 344px;
    width: 1px;
    height: 22px;
    background: var(--muted);
  }
  .icon { display: block; }
</style>
</head>
<body>
  <main class="stage">
    <section class="card" aria-label="Business card">
      <p class="holder-name">Marta Quorrin</p>
      <p class="holder-role">Owner / Designer</p>
      <h1 class="wordmark">Vellorine</h1>

      <svg class="bracket" width="380" height="26" viewBox="0 0 380 26" aria-hidden="true">
        <path d="M1 0 V24 H378 V8" fill="none" stroke="var(--rule)" stroke-width="2"/>
      </svg>

      <p class="contact contact-phone">
        <svg class="icon" width="16" height="16" viewBox="0 0 16 16" aria-hidden="true">
          <rect x="1" y="1" width="14" height="14" fill="none" stroke="var(--ink)" stroke-width="1.5"/>
          <path d="M5 4 h2 l1 3 -1.5 1 a6 6 0 0 0 2.5 2.5 l1-1.5 3 1 v2 a1 1 0 0 1 -1 1 A8 8 0 0 1 4 5 a1 1 0 0 1 1-1z" fill="var(--ink)" transform="scale(0.85) translate(1.4 1.4)"/>
        </svg>
        <span>555-203-7718</span>
      </p>
      <span class="contact-divider" aria-hidden="true"></span>
      <p class="contact contact-email">
        <svg class="icon" width="18" height="14" viewBox="0 0 18 14" aria-hidden="true">
          <rect x="1" y="1" width="16" height="12" fill="none" stroke="var(--ink)" stroke-width="1.5"/>
          <path d="M1 1 L9 8 L17 1" fill="none" stroke="var(--ink)" stroke-width="1.5"/>
        </svg>
        <span>mquorrin@vmail.com</span>
      </p>
    </section>
  </main>
</body>
</html>
```